Community-based social network needs a new landing page

We need a landing page for a local social network in Singapore called "LaneSharely.sg". It is a website that help neighbours to connect with each other for mutual benefits such as providing professional/non-professional services, sharing items, and neighbourly help, etc.

There is an existing website but we want to completely revamp it. It is most important that the new landing page communicates that the neighbourhood has skills and services for people to discover.

The final design of the landing page should be modern, and communicates a sense of community and vibrancy. As a matter of priority, more real estate should be accorded to the neighbours providing services elements.

We have drafted 2 reference sites that communicates the key ideas/user propositions for your easy reference:
http://tavrelko82.exampleweb.com/lanesharely
http://tavrelko82.exampleweb.com/lanesharely2

As long as the key ideas/user propositions are kept to, we are open to any design proposals. I.e. you do not have to follow the design layout of the reference sites

Target Market(s)

Our target market is primarily the Singapore community, includes all genders, education levels and occupations, aged between 17-45 years old.

In the file uploaded, you will find pictures of Singapore neighbourhoods and people of local ethnicities. Please use them, but you may arrange and add further filters to better enhance them

Industry/Entity Type

Real Estate

Requirements
Nice to have
• Landing page could be similar to that of www.gatherova.com, not just at the top, but also the way the other categories are presented at the bottom.

```html
<!DOCTYPE html>
<html lang="en">
<head>
<meta charset="utf-8">
<title>LaneSharely.sg</title>
<link rel="stylesheet" href="https://fonts.googleapis.com/css2?family=Arimo:wght@400;700&display=swap">
<style>
:root{
  --red:#c8372a;
  --red-dark:#b32c20;
  --tan:#c49a6c;
  --page:#f0f0f0;
  --brown:#4a3728;
  --icon:#5a3d26;
  --ink:#222;
  --muted:#555;
  --panel:rgba(235,238,242,.82);
  --field:rgba(245,245,245,.9);
  --white:#fff;
}
*{box-sizing:border-box;margin:0;padding:0}
html,body{width:1017px;height:1200px;overflow:hidden;background:var(--page)}
body{font-family:"Arimo",Arial,sans-serif;color:var(--ink)}
.stage{position:absolute;left:0;top:0;width:1000px;height:1180px;transform:scale(1.017,1.0169);transform-origin:0 0;background:var(--page)}
.abs{position:absolute}

/* header */
.site-header{left:0;top:0;width:1000px;height:100px;background:var(--red);box-shadow:0 2px 4px rgba(0,0,0,.3);z-index:2}
.brand{left:31px;top:20px;width:209px;height:42px;background:var(--white);display:flex;align-items:center;gap:8px;padding-left:8px;font-size:22px;font-weight:700;color:var(--red);letter-spacing:-.5px}
.brand-dot{width:18px;height:18px;border-radius:50%;background:var(--red)}
.header-actions{right:29px;top:69px;display:flex;gap:3px}
.header-actions span{background:var(--white);color:var(--red);height:31px;display:flex;align-items:center;justify-content:center;font-weight:700}
.social-name{width:62px;font-size:12px}
.header-login{width:56px;font-size:16px}

/* hero */
.hero{left:0;top:100px;width:1000px;height:490px;background:linear-gradient(180deg,#5d7fb0 0%,#9bb2cf 22%,#e8e2d2 40%,#d9cfbb 62%,#8a6c55 76%,#2f4a26 92%,#2c4322 100%)}
.panel{background:var(--panel);border-radius:3px}
.login-panel{left:40px;top:115px;width:170px;height:100px}
.field{position:absolute;background:var(--field);font-size:13px;color:#444;padding:5px 8px;height:24px}
.btn{position:absolute;background:var(--red);color:var(--white);font-size:12px;display:flex;align-items:center;justify-content:center}
.signup-panel{left:40px;top:245px;width:210px;height:160px}
.signup-title{position:absolute;left:10px;top:12px;color:var(--red);font-size:13px}
.offers-panel{left:700px;top:115px;width:250px;height:280px}
.offer-photo{position:absolute;left:20px;width:58px;height:78px;background:linear-gradient(180deg,#c9c9c9,#8d8f92)}
.offer-text{position:absolute;left:82px;width:146px;background:rgba(248,248,248,.95);font-size:10.5px;line-height:14px;padding:4px 10px}

/* categories */
.category{width:210px;height:180px}
.category-back{position:absolute;inset:0;background:var(--red);transform:rotate(-3deg) translate(2px,4px)}
.category-card{position:absolute;inset:0;background:var(--tan);text-align:center;padding:14px 16px 0}
.category-card h2{font-weight:400;font-size:15px;color:var(--red);line-height:19px;padding-bottom:6px;border-bottom:1px dashed #4a3728;margin:0 -8px 6px}
.category-card p{font-size:11.5px;line-height:14.5px;color:#4a3a2a}
.category-card .btn{left:85px;bottom:10px;width:40px;height:24px;font-size:12px}

.rule{left:5px;top:809px;width:995px;border-top:1px dashed var(--red)}
.footer-nav{top:829px;left:330px;display:flex;gap:38px;font-size:11px;color:var(--red)}

.col-title{color:var(--red);font-weight:700;font-size:16px}
.media-quote{left:58px;top:906px;font-size:12px;line-height:16px;color:var(--red)}
.post{left:388px;display:flex;align-items:flex-start;gap:6px;font-size:10.5px;line-height:14.5px;width:250px}
.post svg{flex:none}
.members{left:684px;top:897px;display:grid;grid-template-columns:repeat(6,32px);grid-auto-rows:32px;gap:4px 4px}
.members i{display:block}

.site-footer{left:0;top:1080px;width:1000px;height:100px;background:var(--brown);box-shadow:0 -2px 4px rgba(0,0,0,.25);color:var(--white)}
.legal{left:20px;top:28px;font-size:9.5px;line-height:14px;width:510px}
.keep{right:31px;top:16px;font-weight:700;font-size:15px}
.keep-links{right:38px;top:40px;display:flex;gap:10px}
.keep-links span{background:var(--red);height:30px;padding:0 5px;display:flex;align-items:center;font-size:10px;font-weight:700;color:var(--white)}
</style>
</head>
<body>
<div class="stage">

  <header class="site-header abs">
    <div class="brand abs"><span class="brand-dot"></span>LaneSharely.sg</div>
    <div class="header-actions abs"><span class="social-name">Circlio</span><span class="header-login">Login</span></div>
  </header>

  <div class="hero abs" role="img" aria-label="Photo of tall public housing blocks under a cloudy blue sky with trees in front"></div>

  <form class="login-panel panel abs">
    <div class="field" style="left:11px;top:9px;width:150px">Username</div>
    <div class="field" style="left:11px;top:46px;width:150px">Password</div>
    <div class="btn" style="left:110px;top:80px;width:49px;height:20px">Login</div>
  </form>

  <form class="signup-panel panel abs">
    <div class="signup-title">Sign up</div>
    <div class="field" style="left:9px;top:35px;width:190px">Display Name</div>
    <div class="field" style="left:9px;top:68px;width:190px">Email Address</div>
    <div class="field" style="left:9px;top:100px;width:190px">Password</div>
    <div class="btn" style="left:8px;top:135px;width:32px;height:25px;font-size:8px">Circlio</div>
    <div class="btn" style="left:42px;top:135px;width:68px;height:25px;font-size:13px">Connect</div>
    <div class="btn" style="left:115px;top:135px;width:88px;height:25px;font-size:11.5px">Create Account</div>
  </form>

  <aside class="offers-panel panel abs">
    <div class="offer-photo" style="top:11px" role="img" aria-label="Photo of a woman holding a mop"></div>
    <div class="offer-text" style="top:20px">Melissa is offering hourly housekeeping at $13 per hour</div>
    <div class="offer-photo" style="top:91px" role="img" aria-label="Portrait photo of a smiling woman"></div>
    <div class="offer-text" style="top:99px;padding-top:6px">Jia Hui is offering professional home-call beauty services at low rates</div>
    <div class="offer-photo" style="top:179px" role="img" aria-label="Photo of a student holding folders"></div>
    <div class="offer-text" style="top:193px;padding-top:6px">Pei Ling, an architecture undergraduate, will design your home from only $200</div>
  </aside>

  <section class="category abs" style="left:123px;top:610px">
    <div class="category-back"></div>
    <div class="category-card">
      <h2>Professional Services</h2>
      <p>If you're a professional service provider, take a FREE listing here and offer a "neighbour rate" to the people living near you!</p>
      <div class="btn">GO</div>
    </div>
  </section>
  <section class="category abs" style="left:392px;top:610px">
    <div class="category-back"></div>
    <div class="category-card">
      <h2>Non-Professional</h2>
      <p>You may be a student, enthusiast or just someone with time and muscle, but you may be good enough for your neighbours to hire! Take a FREE listing here!</p>
      <div class="btn">GO</div>
    </div>
  </section>
  <section class="category abs" style="left:652px;top:610px">
    <div class="category-back"></div>
    <div class="category-card" style="padding-top:6px">
      <h2>Selling, helping, lending and borrowing</h2>
      <p>Let's contribute stuff and effort into the neighbourhood pool. We can all save money, reduce wastage and be kind to the environment.</p>
      <div class="btn">GO</div>
    </div>
  </section>

  <div class="rule abs"></div>
  <nav class="footer-nav abs"><span>ABOUT US</span><span>FAQ</span><span>TERMS OF USE</span><span>PRIVACY POLICY</span><span>CONTACT US</span></nav>

  <h3 class="col-title abs" style="left:58px;top:885px">MEDIA MENTIONS</h3>
  <p class="media-quote abs">"Website to help neighbours share household items"<br>- The Harbour Daily</p>

  <h3 class="col-title abs" style="left:388px;top:869px">LATEST POSTS</h3>
  <div class="post abs" style="top:894px">
    <svg width="34" height="24" viewBox="0 0 34 24"><rect x="2" y="6" width="10" height="15" rx="2" fill="var(--icon)" transform="rotate(-20 7 13)"/><rect x="16" y="2" width="14" height="20" rx="2" fill="var(--icon)"/><rect x="19" y="6" width="8" height="9" fill="#f0f0f0"/></svg>
    <span style="padding-top:5px">KelvinL is selling Micro/Nano Sim Adapters</span>
  </div>
  <div class="post abs" style="top:930px">
    <svg width="34" height="34" viewBox="0 0 34 34"><polygon points="22,2 8,20 16,20 4,33 28,13 19,13 27,2" fill="var(--icon)"/></svg>
    <span style="padding-top:9px">JTK wants to offer Electrical Repair (DIY)</span>
  </div>
  <div class="post abs" style="top:967px">
    <svg width="34" height="26" viewBox="0 0 34 26"><rect x="10" y="8" width="16" height="14" rx="2" fill="var(--icon)"/><polygon points="10,12 1,2 3,1 12,9" fill="var(--icon)"/><path d="M26 10 q7 2 0 10" stroke="var(--icon)" stroke-width="2" fill="none"/></svg>
    <span>Marcus Tan wants to offer help water your plants while you're overseas! I'm dependable and detailed.</span>
  </div>
  <div class="post abs" style="top:1019px">
    <svg width="34" height="28" viewBox="0 0 34 28"><g stroke="var(--icon)" stroke-width="2"><line x1="14" y1="1" x2="9" y2="27"/><line x1="21" y1="1" x2="18" y2="27"/><line x1="13" y1="7" x2="20" y2="7"/><line x1="12" y1="14" x2="19" y2="14"/><line x1="11" y1="21" x2="18" y2="21"/></g></svg>
    <span style="padding-top:8px">FaridZ has shared Ladder</span>
  </div>

  <h3 class="col-title abs" style="left:684px;top:864px">LATEST MEMBERS</h3>
  <div class="members abs" role="img" aria-label="Grid of recent member profile pictures">
    <i style="background:#8a7a66"></i><i style="background:#6f8a5c"></i><i style="background:#9a9a9a"></i><i style="background:#3a3550"></i><i style="background:#6a6f80"></i><i style="background:#d8b5c8"></i>
    <i style="background:#7d6a58"></i><i style="background:#9fb4c6"></i><i style="background:#a7a7a0"></i><i style="background:#b49462"></i><i style="background:#d7c7b0"></i><i style="background:#c7c9c0"></i>
    <i style="background:#8c5d44"></i><i style="background:#4f6a3c"></i><i style="background:#4c5a6c"></i><i style="background:#9c7a5a"></i><i style="background:#b08f7a"></i><i style="background:#6c5a50"></i>
    <i style="background:#556070"></i><i style="background:#3c3c3c"></i><i style="background:#8a8a8a"></i><i style="background:#5a4a46"></i><i style="background:#a05a7a"></i><i style="background:#2a2a2a"></i>
  </div>

  <footer class="site-footer abs">
    <p class="legal abs">© Kampongrid Pte Ltd 2013<br>LaneSharely.sg is a website of Kampongrid Pte Ltd. We help you pool together physical items, efforts, and purchasing power with your favourite neighbours so that you can save money, free up space at home, be eco-friendly.</p>
    <div class="keep abs">KEEP IN TOUCH</div>
    <div class="keep-links abs"><span>Circlio</span><span>Chirpa</span><span>Plusly</span></div>
  </footer>

</div>
</body>
</html>
```